Business Card Design for drone videography and photography

I have a Vexor Talon 3 drone. I am looking for a logo to somehow incorporate with my business name. I don't even know what is an appropriate font. I am most filming real estate homes. I want something simplistic and a logo that makes sense for the business that I'm in. xxxxxxxxxxxxxxxxxxxxxxxxxxxxxxxxxxxxxxxxxxxxxxxxxxxxxxxxxxxxxxxxxxxxxxxxxxxxxxxxxxxxxxxxxxxxxxxxxxxxxxxxxxxxxxxxxxxxxxxxxxxxxxxxxxxxxxxxxxxxxxxxxxxxxxxxxxxxxxxxxxxxxxxxxxxxxxxxxxxxxxxxxxxxxxxxxxxxxxxxxxxxxxxxxxxxxxxxxxxxxxxxxxxxxxxxxxxxxxxxxxxxxxxxxxxxxxxxxxxxxxxxxxxxxxxxxxxxxxxxxxxxxxxxxxxxxxxxxxxxxxxxxxxxxxxxxxxxxxxxxxxxxxxxxxxxxxxxxxxxxxxxxxxxxxxxxxxxxxxxxxxxxxxxxxxxxxxxxxxxxxxxxxxxxxxxxxxxxxxxxxxxxxxxxxxxxxxxxxxxxxxxxxxxxxxxxxxxxxxxxxxxxxxxxxxxxxxxxxxxxxxxxxxxxxxxxxxxxxxxxxxxxxxxxxxxxxxxxxxxxxxxxxxxxxxxxxxxxxxxxxxxxxxxxxxxxxxxxxxxxxxxxxxxxxxxxxxxxxxxxxxxxxxxxxxxxxxxxxxxxxxxxxxxxxxxxxxxxxxxxxxxxxxxxxxxxxxxxxxxxxxxxxxxxxxxxxxxxxxxxxxxxxxxxxxxxxxxxxxxxxxxxxxxxxxxxxxxxxxxxxxxxxxxxxxxxxxxxxxxxxxxxxxxxxxxxxxxxxxxxxxxxxxxxxxxxxxxxxxxxxxxxxxxxxxxxxxxxxxxxxxxxxxxxxxxxxxxxxxxxxxxxxxxxxxxxxxxxxxxxxxxxxxxxxxxxxxxxxxxxxxxxxxxxxxxxxxxxxxxxxxxxxxxxxxxxxxxxxxxxxxxxxxxxxxxxxxxxxxxxxxxxxxxxxxxxxxxxxxxxxxxxxxxxxxxxxxxxxxxxxxxxxxxxxxxxxxxxxxxxxxxxxxxxxxxxxxxxxxxxxxxxxxxxxxxxxxxxxxxxxxxxxxxxxxxxxxxxxxxxxxxxxxxxxxxxxxxxxxxxxxxxxxxxxxxxxxxxxxx

Target Market(s)

Real estate

Industry/Entity Type

Business

Contact Information for Business Card

BRANDT SKYVIEW STUDIO
Daniel Brandt
Owner/Operator

48305 Birch Way
Larkfield MO 63512

314-720-4163
dbrandt@brandtskyviewstudio.example

NCQ Drone Certified
Insured
Section 333 Exempt
Halvo Wing Class Certified

Font styles to use
Other font styles liked:
• PUMP DEMI BOLD LET

Requirements
Must have
• Maybe have the certifications on the back??? The business card must be more serious than playful
Nice to have
• Possibly have the logo work itself into the business name?
Should not have
• nothing that looks like a "fun" business. I want this business card to look professional but also simplistic. I don't want a picture that I took from my drone as the background.

```html
<!DOCTYPE html>
<html lang="en">
<head>
<meta charset="utf-8">
<title>Brandt Skyview Studio – Business Card</title>
<link rel="stylesheet" href="https://fonts.googleapis.com/css2?family=Open+Sans:wght@400;600;700&display=swap">
<style>
  :root {
    --backdrop-top: #ababab;
    --backdrop-bottom: #8a8a8a;
    --card-light: #ffffff;
    --card-dark: #231f20;
    --ink: #231f20;
    --ink-soft: #555555;
    --ink-reverse: #ffffff;
  }
  * { margin: 0; padding: 0; box-sizing: border-box; }
  html, body { width: 1200px; height: 900px; overflow: hidden; }
  body {
    position: relative;
    background: linear-gradient(180deg, var(--backdrop-top), var(--backdrop-bottom));
    font-family: "Open Sans", Arial, sans-serif;
  }
  .card {
    position: absolute;
    top: 170px;
    width: 347px;
    height: 561px;
    text-align: center;
  }
  .card-front { left: 259px; background: var(--card-light); color: var(--ink); }
  .card-back { left: 631px; background: var(--card-dark); color: var(--ink-reverse); }

  .tab {
    position: absolute;
    left: 102px;
    width: 143px;
    background: var(--card-dark);
  }
  .tab-top { top: 0; height: 30px; }
  .tab-bottom { bottom: 0; height: 28px; }

  .brand {
    position: absolute;
    left: 0; right: 0;
    top: 112px;
    display: flex;
    flex-direction: column;
    align-items: center;
  }
  .brand-dot {
    width: 30px; height: 30px;
    border-radius: 50%;
    border: 4px solid currentColor;
    margin-bottom: 14px;
  }
  .brand-name {
    font-weight: 700;
    font-size: 26px;
    line-height: 32px;
    letter-spacing: 2px;
  }

  .contact {
    position: absolute;
    left: 0; right: 0;
    top: 306px;
    font-size: 14.5px;
    line-height: 20px;
    color: var(--ink-soft);
  }
  .contact-name { font-size: 18px; font-weight: 700; color: var(--ink); line-height: 24px; }
  .contact-role { margin-bottom: 14px; }
  .contact-address { margin-bottom: 15px; }
  .contact-line { display: flex; align-items: center; justify-content: center; gap: 8px; }
  .contact-line svg { fill: var(--ink); flex: none; }

  .credentials {
    position: absolute;
    left: 0; right: 0;
    top: 384px;
    font-size: 15px;
    font-weight: 600;
    line-height: 20px;
  }
  .credentials p + p { margin-top: 17px; }
</style>
</head>
<body>
  <section class="card card-front">
    <div class="tab tab-top"></div>
    <div class="brand">
      <span class="brand-dot"></span>
      <div class="brand-name">BRANDT<br>SKYVIEW STUDIO</div>
    </div>
    <div class="contact">
      <p class="contact-name">Daniel Brandt</p>
      <p class="contact-role">Owner/Operator</p>
      <p class="contact-address">48305 Birch Way<br>Larkfield MO 63512</p>
      <p class="contact-line">
        <svg width="11" height="11" viewBox="0 0 24 24" aria-hidden="true"><path d="M6.6 10.8a15.1 15.1 0 0 0 6.6 6.6l2.2-2.2c.3-.3.7-.4 1-.2 1.1.4 2.3.6 3.6.6.6 0 1 .4 1 1V20c0 .6-.4 1-1 1A17 17 0 0 1 3 4c0-.6.4-1 1-1h3.5c.6 0 1 .4 1 1 0 1.3.2 2.5.6 3.6.1.3 0 .7-.2 1z"/></svg>
        314-720-4163
      </p>
      <p class="contact-line">
        <svg width="11" height="9" viewBox="0 0 22 16" aria-hidden="true"><path d="M0 0h22v16H0zM2 2v.6l9 6 9-6V2zm0 2.9V14h18V4.9l-9 6z"/></svg>
        dbrandt@brandtskyviewstudio.example
      </p>
    </div>
    <div class="tab tab-bottom"></div>
  </section>

  <section class="card card-back">
    <div class="brand">
      <span class="brand-dot"></span>
      <div class="brand-name">BRANDT<br>SKYVIEW STUDIO</div>
    </div>
    <div class="credentials">
      <p>NCQ Drone Certified<br>Insured</p>
      <p>Section 333 Exempt<br>Halvo Wing Class Certified</p>
    </div>
  </section>
</body>
</html>
```